BrimKeel Limited needs a business card design

We need a business card design that reflects both professionalism and innovation and captures our brand identity. We provide online enterprise solutions to HR and executive management. We would like to use the colors in our logo (Blue and Orange). See attached file.

We would like a more creative design than the existing attached business card but maintain the same information on it.

To see our products site, please visit www.brimkeel.example which reflects more our identity
Updates

Please see our site: www.brimkeel.example, not www.brimkeel.example.co.uk for our colors and look and feel

Target Market(s)

Senior Executives

Industry/Entity Type

Business

Requirements
Must have
• Logo and use of logo colors
Nice to have
• Icons
Should not have
• Images

```html
<!DOCTYPE html>
<html lang="en">
<head>
<meta charset="utf-8">
<title>BrimKeel Limited – Business Card</title>
<link href="https://fonts.googleapis.com/css2?family=Didact+Gothic&display=swap" rel="stylesheet">
<style>
  :root {
    --orange: #ec7424;
    --orange-deep: #e0651c;
    --blue: #1f78c0;
    --blue-light: #3a8fd0;
    --ink-grey: #6a6a6a;
    --paper: #ffffff;
    --backdrop: #ecebe8;
    --card-font: "Didact Gothic", "Century Gothic", sans-serif;
  }
  * { box-sizing: border-box; margin: 0; padding: 0; }
  html, body {
    width: 1200px; height: 1184px; overflow: hidden;
    background: var(--backdrop);
    font-family: var(--card-font);
  }
  .canvas {
    position: relative; width: 1200px; height: 1184px;
  }
  .card {
    position: absolute; left: 150px; width: 900px; height: 514px;
    box-shadow: 0 10px 30px rgba(0,0,0,.18);
  }

  /* Front */
  .card--front {
    top: 60px;
    background: linear-gradient(120deg, var(--orange) 0%, var(--orange-deep) 100%);
    color: var(--paper);
    text-align: center;
  }
  .front__company {
    position: absolute; top: 44px; left: 0; right: 0;
    color: var(--blue); font-size: 38px; letter-spacing: .5px;
  }
  .front__tagline {
    position: absolute; top: 100px; left: 0; right: 0;
    font-size: 19px; letter-spacing: 1.5px; text-transform: uppercase;
  }
  .front__wordmark {
    position: absolute; top: 150px; left: 0; right: 0;
    color: var(--blue); font-size: 150px; line-height: 1; letter-spacing: -2px;
  }
  .front__legal {
    position: absolute; bottom: 44px; left: 0; right: 0;
    font-size: 16px; line-height: 1.6; letter-spacing: .3px;
  }

  /* Back */
  .card--back {
    top: 610px;
    background: var(--paper);
  }
  .back__wordmark {
    position: absolute; top: 48px; left: 60px;
    color: var(--blue); font-size: 96px; line-height: 1; letter-spacing: -1px;
  }
  .person { position: absolute; top: 226px; left: 100px; }
  .person__name {
    font-size: 34px; letter-spacing: 1px; text-transform: uppercase;
  }
  .person__first { color: var(--blue); }
  .person__last { color: var(--orange); }
  .person__role {
    margin-top: 4px; color: var(--ink-grey);
    font-size: 18px; letter-spacing: 4px; text-transform: uppercase;
  }
  .contact-list { position: absolute; list-style: none; color: var(--ink-grey); }
  .contact-list--online { top: 356px; left: 100px; font-size: 21px; }
  .contact-list--online li { display: flex; align-items: center; gap: 16px; margin-bottom: 16px; }
  .contact-list--office { top: 150px; left: 520px; font-size: 19px; line-height: 1.45; }
  .contact-row { display: flex; gap: 16px; margin-bottom: 24px; }
  .contact-row svg { flex: none; margin-top: 4px; }
  .icon { width: 20px; height: 20px; fill: var(--orange); }
</style>
</head>
<body>
<main class="canvas">

  <section class="card card--front" aria-label="Card front">
    <h1 class="front__company">BrimKeel Limited</h1>
    <p class="front__tagline">Developing leaders and organisations</p>
    <p class="front__wordmark">BrimKeel</p>
    <p class="front__legal">
      BrimKeel Limited is a company registered in England &amp; Wales No. 0000000<br>
      Registered Office: Quay House, 4 Mill Lane, London
    </p>
  </section>

  <section class="card card--back" aria-label="Card back">
    <p class="back__wordmark">BrimKeel</p>

    <div class="person">
      <h2 class="person__name"><span class="person__first">Mara</span><span class="person__last">Tollen</span></h2>
      <p class="person__role">Managing Director</p>
    </div>

    <ul class="contact-list contact-list--online">
      <li>
        <svg class="icon" viewBox="0 0 20 20" aria-hidden="true"><rect x="1" y="4" width="18" height="12" rx="1"/><path d="M2 5 L10 11 L18 5" stroke="#fff" stroke-width="1.6" fill="none"/></svg>
        mtollen@brimkeel.example.co.uk
      </li>
      <li>
        <svg class="icon" viewBox="0 0 20 20" aria-hidden="true"><circle cx="10" cy="10" r="9"/><g stroke="#fff" stroke-width="1.2" fill="none"><ellipse cx="10" cy="10" rx="4" ry="9"/><line x1="1" y1="10" x2="19" y2="10"/><line x1="3" y1="5.5" x2="17" y2="5.5"/><line x1="3" y1="14.5" x2="17" y2="14.5"/></g></svg>
        www.brimkeel.example.co.uk
      </li>
    </ul>

    <ul class="contact-list contact-list--office">
      <li class="contact-row">
        <svg class="icon" viewBox="0 0 20 20" aria-hidden="true"><path d="M10 1 C5.5 1 3 4.3 3 7.6 C3 12 10 19 10 19 C10 19 17 12 17 7.6 C17 4.3 14.5 1 10 1 Z"/><circle cx="10" cy="7.6" r="2.6" fill="#fff"/></svg>
        <address style="font-style:normal">brimkeel limited<br>&nbsp;&nbsp;22 Harlow Court,<br>&nbsp;&nbsp;118 Fenwick Rd, London, N4 7QT</address>
      </li>
      <li class="contact-row">
        <svg class="icon" viewBox="0 0 20 20" aria-hidden="true"><path d="M5 1.5 L8 5.5 L6.3 7.6 C7.4 10 9.9 12.6 12.4 13.7 L14.5 12 L18.5 15 L16.6 18 C9.5 18.4 1.6 10.5 2 3.4 Z"/></svg>
        <span>&nbsp;&nbsp;+44 20 7946 0321<br>&nbsp;&nbsp;+1 555 014 2290<br>&nbsp;&nbsp;+961 70 555 012</span>
      </li>
    </ul>
  </section>

</main>
</body>
</html>
```